Corporate Values project needs own identity (logo, illustrations, font)

For a project to liven up corporate values we have designed 10 questions our employees should ask themselves at any time. To start marketing these, we want to have various outings (posters, cards, leaflets, etc) that illustrate these questions. preferably with a logo / font of its own. Look and feel / moodwords: insurance, blue, values, non negociable, fun, vintage, together. The 10 questions are:
1. What would the customer say?
2. How will this help those of us in front of the customer?
3. Have I expressed my views clearly and openly?
4. How can we do this differently and to higher standards? Better, faster, simpler?
5. How can I help, beyond my specific role description?
6. Have I recognised other people’s contributions and ideas?
7. Am I keeping my commitments to others, internal or externally?
8. How can I learn more? And how can I share more so others can learn form this?
9. Who needs, and who does not need to be involved?
10. Is there a different or alternative view, opinion or option?

Preferably, each question gets its own little ilustration.

If things are not clear, or more information needed, please let me know.

Reason: Since part of the project has been postponed, we can take more time for the design.

```html
<!DOCTYPE html>
<html lang="en">
<head>
<meta charset="utf-8">
<title>Question 2 of 10 – How can I help</title>
<link rel="stylesheet" href="https://fonts.googleapis.com/css2?family=Oswald:wght@200;400;700&display=swap">
<style>
  :root {
    --teal: #00b2b5;
    --track: #00c9cc;
    --cyan: #14f4f7;
    --white: #ffffff;
  }
  html, body {
    margin: 0;
    padding: 0;
    overflow: hidden;
    background: var(--teal);
  }
  .card {
    position: relative;
    width: 1200px;
    height: 1000px;
    background: var(--teal);
    overflow: hidden;
  }
  .progress {
    position: absolute;
    left: 37px;
    top: 38px;
    width: 809px;
    height: 6px;
    background: var(--track);
  }
  .progress__fill {
    width: 161px;
    height: 100%;
    background: var(--cyan);
  }
  .question {
    position: absolute;
    inset: 0;
    width: 1200px;
    height: 1000px;
  }
  .question__count {
    font-family: "Oswald", sans-serif;
    font-weight: 400;
    font-size: 54px;
    fill: var(--cyan);
  }
  .question__lead {
    font-family: "Oswald", sans-serif;
    font-weight: 700;
    font-size: 146px;
    fill: var(--white);
  }
  .question__rest {
    font-family: "Oswald", sans-serif;
    font-weight: 200;
    font-size: 146px;
    fill: var(--white);
  }
  .motif {
    position: absolute;
    left: 60px;
    top: 712px;
    width: 500px;
    height: 126px;
  }
  .motif__art {
    fill: var(--cyan);
    opacity: 0.55;
  }
  .motif__arrow {
    fill: none;
    stroke: var(--cyan);
    stroke-width: 8;
    stroke-linecap: round;
    stroke-linejoin: round;
  }
</style>
</head>
<body>
  <main class="card">
    <div class="progress"><div class="progress__fill"></div></div>

    <svg class="question" viewBox="0 0 1200 1000" aria-labelledby="q-title">
      <text class="question__count" x="37" y="125">2/10</text>
      <text id="q-title">
        <tspan class="question__lead" x="38" y="310">HOW CAN I HELP,</tspan>
        <tspan class="question__rest" x="38" y="442">BEYOND MY SPECIFIC</tspan>
        <tspan class="question__rest" x="38" y="575">ROLE DESCRIPTION?</tspan>
      </text>
    </svg>

    <svg class="motif" viewBox="0 0 500 126">
      <rect class="motif__art" x="5" y="18" width="145" height="90" rx="12"
            role="img" aria-label="Line drawing of a pair of reading glasses"></rect>
      <path class="motif__arrow" d="M199 63 H283 M264 44 L283 63 L264 82"></path>
      <rect class="motif__art" x="342" y="6" width="148" height="114" rx="12"
            role="img" aria-label="Line drawing of a superhero chest emblem"></rect>
    </svg>
  </main>
</body>
</html>
```